Modernisierter Briefkopf für Dienstleistungsunternehmen im Bereich IT-Sicherheitsberatung & Datenschutz
Zielgruppe
Wir haben folgende Dienstleistungen:
Managed Services, IT-Sicherheitsberatung, Datenschutz, Datenschutzbeauftragter,Schulungen,
Kunden sind hauptsächlich Firmen
Aufgabenstellung
siehe Dateiupload, das KORV-Logo soll natürlich weiterhin vorkommen. Den aktuellen Briefkopf habe ich auch hochgeladen.
Das ganze müsste etwas moderner werden.

```html
<!DOCTYPE html>
<html lang="de">
<head>
<meta charset="utf-8">
<title>KORV Briefkopf</title>
<link href="https://fonts.googleapis.com/css2?family=Open+Sans:wght@300;400;700&display=swap" rel="stylesheet">
<style>
  :root {
    --bg: #e9e9e9;
    --paper: #f6f6f6;
    --green: #0e9a3a;
    --green-light: #6ab66b;
    --green-dark: #0a6b2c;
    --ink: #2b2b2b;
    --muted: #5d5d5d;
    --rule: #c9c9c9;
  }
  * { box-sizing: border-box; margin: 0; padding: 0; }
  html, body { width: 1200px; height: 1010px; overflow: hidden; }
  body {
    background: var(--bg);
    font-family: "Open Sans", Arial, sans-serif;
    color: var(--ink);
  }
  .letter {
    position: absolute;
    left: 260px; top: 24px;
    width: 680px; height: 962px;
    background: var(--paper);
    box-shadow: 0 6px 24px rgba(0,0,0,.18);
    overflow: hidden;
  }
  .band {
    position: absolute; left: 0; width: 100%;
    background: linear-gradient(90deg, var(--green-light) 0%, var(--green) 55%, var(--green-light) 100%);
  }
  .band--top { top: 0; height: 14px; border-bottom: 3px solid var(--green-dark); }
  .band--bottom { bottom: 0; height: 36px; border-top: 3px solid var(--green-dark); }
  .band__brand {
    position: absolute; right: 24px; top: 7px;
    display: flex; align-items: center; gap: 6px;
    color: #fff; font-size: 13px; font-weight: 400; letter-spacing: .08em;
  }
  .band__brand .mark { width: 12px; height: 12px; border: 1.5px solid #fff; }

  .sender-line {
    position: absolute; left: 62px; top: 128px;
    font-size: 9px; font-weight: 300; font-style: normal; color: var(--muted);
  }

  .contact {
    position: absolute; right: 34px; top: 58px;
    display: flex; gap: 14px;
  }
  .contact__company { text-align: right; width: 205px; font-size: 9.5px; line-height: 1.38; }
  .brand {
    display: inline-flex; align-items: center; gap: 6px;
    color: var(--green); font-size: 22px; font-weight: 400; letter-spacing: .12em;
    margin-bottom: 6px;
  }
  .brand .mark { width: 14px; height: 14px; border: 1.5px solid var(--green); }
  .tagline { font-weight: 700; color: var(--ink); margin-bottom: 6px; }
  .services { list-style: none; color: var(--muted); font-weight: 300; }
  .contact__divider { width: 1px; background: var(--rule); }
  .contact__person { width: 160px; font-size: 9.5px; line-height: 1.38; color: var(--muted); }
  .contact__person .name { font-weight: 700; color: var(--ink); }
  .contact__group { margin-top: 6px; display: grid; grid-template-columns: 14px 1fr; column-gap: 4px; align-items: start; }
  .contact__group svg { width: 10px; height: 10px; margin-top: 2px; }

  .body {
    position: absolute; left: 62px; top: 250px; width: 560px;
    font-size: 11.5px; line-height: 1.5;
  }
  .salutation { margin-bottom: 12px; }
  .body p { margin-bottom: 12px; }
  .closing { margin-top: 18px; }
  .signature {
    margin-top: 8px; width: 150px; height: 56px;
    background: linear-gradient(135deg, #ffffff, #e8e8e8);
  }
</style>
</head>
<body>
  <main class="letter">
    <div class="band band--top"></div>

    <div class="sender-line">KORV | Hafenkamp 7 | 24103 Kiel</div>

    <section class="contact">
      <div class="contact__company">
        <div class="brand"><span class="mark"></span>KORV</div>
        <div class="tagline">Ihr Partner für IT- und<br>Telekommunikationslösungen</div>
        <ul class="services">
          <li>Managed Services</li>
          <li>IT-Sicherheitsberatung</li>
          <li>Datenschutz</li>
          <li>Datenschutzbeauftragter</li>
          <li>Schulungen</li>
        </ul>
      </div>
      <div class="contact__divider"></div>
      <div class="contact__person">
        <div class="name">Jana Brinkmann</div>
        <div>Hafenkamp 7</div>
        <div>24103 Kiel</div>
        <div class="contact__group">
          <svg viewBox="0 0 10 10" aria-hidden="true"><path d="M2 1l2 2-1 1c.5 1.3 1.7 2.5 3 3l1-1 2 2-1.5 1.5C4.5 9 1 5.5.5 2.5z" fill="var(--green)"/></svg><span>+49 431 555 20 10</span>
          <svg viewBox="0 0 10 10" aria-hidden="true"><rect x="2.5" y="0.5" width="5" height="9" rx="1" fill="none" stroke="var(--green)"/></svg><span>+49 170 555 38 42</span>
          <svg viewBox="0 0 10 10" aria-hidden="true"><rect x="1" y="4" width="8" height="5" fill="none" stroke="var(--green)"/><rect x="3" y="1" width="4" height="3" fill="none" stroke="var(--green)"/></svg><span>+49 431 555 20 11</span>
        </div>
        <div class="contact__group">
          <svg viewBox="0 0 10 10" aria-hidden="true"><rect x=".5" y="2" width="9" height="6" fill="none" stroke="var(--green)"/><path d="M.5 2l4.5 3.5L9.5 2" fill="none" stroke="var(--green)"/></svg><span>info@korv.example</span>
          <svg viewBox="0 0 10 10" aria-hidden="true"><rect x=".5" y="2" width="9" height="6" fill="none" stroke="var(--green)"/><path d="M.5 2l4.5 3.5L9.5 2" fill="none" stroke="var(--green)"/></svg><span>info@netzwerkhaus.example</span>
          <svg viewBox="0 0 10 10" aria-hidden="true"><circle cx="5" cy="5" r="4.3" fill="none" stroke="var(--green)"/><path d="M.7 5h8.6M5 .7c-2.4 2.6-2.4 6 0 8.6M5 .7c2.4 2.6 2.4 6 0 8.6" fill="none" stroke="var(--green)" stroke-width=".8"/></svg><span>www.korv.example</span>
          <svg viewBox="0 0 10 10" aria-hidden="true"><circle cx="5" cy="5" r="4.3" fill="none" stroke="var(--green)"/><path d="M.7 5h8.6M5 .7c-2.4 2.6-2.4 6 0 8.6M5 .7c2.4 2.6 2.4 6 0 8.6" fill="none" stroke="var(--green)" stroke-width=".8"/></svg><span>www.netzwerkhaus.example</span>
        </div>
      </div>
    </section>

    <article class="body">
      <div class="salutation">Sehr geehrter Herr Mustermann,</div>
      <p>Lorem ipsum dolor sit amet, consectetuer adipiscing elit, sed diam nonummy nibh euismod tincidunt ut laoreet dolore magna aliquam erat volutpat. Ut wisi enim ad minim veniam, quis nostrud exerci tation ullamcorper suscipit lobortis nisl ut aliquip ex ea commodo consequat. Duis autem vel eum iriure dolor in hendrerit in vulputate velit esse molestie consequat, vel illum dolore eu feugiat nulla facilisis at vero eros et accumsan et iusto odio dignissim qui blandit praesent luptatum zzril delenit augue duis dolore te feugait nulla facilisi.</p>
      <p>Lorem ipsum dolor sit amet, cons ectetuer adipiscing elit, sed diam nonummy nibh euismod tincidunt ut laoreet dolore magna aliquam erat volutpat. Ut wisi enim ad minim veniam, quis nostrud exerci tation ullamcorper suscipit lobortis nisl ut aliquip ex ea commodo consequat.</p>
      <p>Lorem ipsum dolor sit amet, consectetuer adipiscing elit, sed diam nonummy nibh euismod tincidunt ut laoreet dolore magna aliquam erat volutpat. Ut wisi enim ad minim veniam, quis nostrud exerci tation ullamcorper suscipit lobortis nisl ut aliquip ex ea commodo consequat. Duis autem vel eum iriure dolor in hendrerit in vulputate velit esse molestie consequat, vel illum dolore eu feugiat nulla facilisis at vero eros et accumsan et iusto odio dignissim qui blandit praesent luptatum zzril delenit augue duis dolore te feugait nulla facilisi.</p>
      <div class="closing">Mit freundlichen Grüßen</div>
      <div class="signature" role="img" aria-label="Handschriftliche Unterschrift"></div>
    </article>

    <div class="band band--bottom">
      <div class="band__brand"><span class="mark"></span>KORV</div>
    </div>
  </main>
</body>
</html>
```